Democracy in crisis book

This book tries to sound the ALARM that we will lose our democracy unless we force Unionists to adopt the plan inside this book. I designed a mock cover (attached) but I am concerned it would not look good in the Thumbnail view that most people would see it as they're scrolling down Shopvale or Pagenook. The final title for the book is: Final Hour to Rescue the Free Republic. The current subtitle is: The Single Path to Halt the 2022 Partisan Takeover & Renew Our Homeland -- but it’s a work in progress.The subtitle is still working progress but it's really not that important and can be small.
STYLE CONSIDERATIONS:
(1) The title should be on 5 separate lines: Final; Hour; To Rescue; Free; Republic
(2) The title could be in white fat letters except for maybe one line that says “To Rescue” which could be in the blue color of the Civic Union Party-- or maybe Free Republic could be in blue. We may have to try a few variations of that.
(3) I picked the red in the mock cover to connotate an emergency,
(4) I liked big bold fat font going across the full page so that it looks like a major warning sign, though note I was unable to extend each line flush all the way to the right which I think would have been better.
(5) I liked it better flush to left instead of centered.
(6) I picked the Harwick monument + a crowd for my mock cover, but a picture of a huge crowd protesting with a picture of the United States Congress in the background would be much better. DO NOT USE HARWICK. Obviously I would need it to be an open license or something I can pay a small amount to get. If you can find that picture then the page should probably be colored in red with Congress in white.
I got the idea 4 giant title from the book “seldom a quiet so bright” and Dellowby’s “When Freedom Fades” or “Grey Herons” by Mara Vostell though I hate that font)
I love Osric Thale’s “marked since the outset” cover so if you find a picture of Congress and a protest crowd instead of painting it red you could have just a couple of jagged red stripes going across it like that cover.
I love the 3-D effect of Greta Wolven's cover for The Silverwren where it looks like a page is being ripped. That effect could be done the words Free Republic like it's being torn off the page UPDATE: MANY DESIGNERS TRIED THAT & IT DID NOT WORK AT ALL.
Note that this book will be submitted to many award competitions, so please give me an award-winning cover.
I like how the title of the book The Unchosen by Martin Fellowes has the words starting to fade. I don't like the ladder on it, but maybe 'Free Republic' could fade like that.
Unionists

```html
<!DOCTYPE html>
<html lang="en">
<head>
<meta charset="utf-8">
<title>Final Hour to Rescue the Free Republic — Book Cover</title>
<link rel="stylesheet" href="https://fonts.googleapis.com/css2?family=Jost:wght@500&family=Playfair+Display:wght@900&family=Oswald:wght@700&display=swap">
<style>
  :root {
    --paper: #f1f1f1;
    --emergency-red: #c8303f;
    --crowd-red-deep: #8e2634;
    --stone-grey: #7c7c7c;
    --stone-dark: #4e4e4e;
    --title-white: #fbf7f7;
    --ink: #0c0c0c;
  }
  html, body {
    margin: 0;
    padding: 0;
    width: 800px;
    height: 1200px;
    overflow: hidden;
    background: var(--paper);
  }
  .book-cover {
    position: relative;
    width: 800px;
    height: 1200px;
    overflow: hidden;
    background: var(--paper);
  }
  .cover-art, .cover-type {
    position: absolute;
    inset: 0;
    width: 800px;
    height: 1200px;
  }
  .subtitle {
    font-family: "Playfair Display", "Times New Roman", serif;
    font-weight: 900;
    font-size: 23px;
    letter-spacing: 1.5px;
    fill: var(--title-white);
  }
  .title-line {
    font-family: "Jost", "Futura", sans-serif;
    font-weight: 500;
    fill: var(--title-white);
  }
  .title-line--faded { fill-opacity: 0.95; }
  .author-name {
    font-family: "Oswald", "Arial Narrow", sans-serif;
    font-weight: 700;
    font-size: 60px;
    fill: var(--ink);
  }
</style>
</head>
<body>
<main class="book-cover">

  <svg class="cover-art" viewBox="0 0 800 1200" xmlns="http://www.w3.org/2000/svg">
    <defs>
      <linearGradient id="crowdRed" x1="0" y1="0" x2="1" y2="1">
        <stop offset="0" stop-color="var(--emergency-red)"/>
        <stop offset="0.55" stop-color="var(--crowd-red-deep)"/>
        <stop offset="1" stop-color="#9a4550"/>
      </linearGradient>
      <linearGradient id="capitolGreyMid" x1="0" y1="0" x2="1" y2="0">
        <stop offset="0" stop-color="#6e6e6e"/>
        <stop offset="0.45" stop-color="var(--stone-dark)"/>
        <stop offset="0.7" stop-color="#8a5f66"/>
        <stop offset="1" stop-color="var(--crowd-red-deep)"/>
      </linearGradient>
      <linearGradient id="capitolGreyLow" x1="0" y1="0" x2="1" y2="0">
        <stop offset="0" stop-color="var(--crowd-red-deep)"/>
        <stop offset="0.2" stop-color="#6a5557"/>
        <stop offset="0.5" stop-color="var(--stone-grey)"/>
        <stop offset="0.8" stop-color="#655658"/>
        <stop offset="1" stop-color="var(--crowd-red-deep)"/>
      </linearGradient>
    </defs>

    <g class="photo-panel photo-panel--crowd" role="img" aria-label="Red-tinted photograph of a dense crowd of protesters">
      <path fill="url(#crowdRed)" d="M0,36 L60,30 L130,40 L210,28 L300,38 L390,26 L470,36 L560,24 L640,34 L720,26 L772,40 L768,140 L778,240 L770,330 L776,430 L780,500 L700,504 L620,512 L540,506 L460,516 L380,510 L300,520 L220,514 L140,524 L60,518 L0,526 Z"/>
    </g>

    <g class="photo-panel photo-panel--capitol-dome" role="img" aria-label="Grey photograph of the Congress dome with protesters at the right">
      <path fill="url(#capitolGreyMid)" d="M0,546 L80,540 L160,548 L250,538 L340,546 L430,536 L520,544 L610,534 L700,542 L778,536 L770,620 L780,700 L772,764 L700,758 L620,766 L540,760 L460,768 L380,762 L300,770 L220,764 L140,770 L60,766 L0,772 Z"/>
    </g>

    <g class="photo-panel photo-panel--capitol-front" role="img" aria-label="Grey photograph of the Congress building facade framed by red-tinted crowds">
      <path fill="url(#capitolGreyLow)" d="M0,790 L80,784 L160,792 L250,782 L340,790 L430,780 L520,788 L610,778 L700,786 L778,780 L770,900 L780,1010 L770,1110 L720,1160 L640,1152 L560,1164 L470,1154 L380,1166 L290,1154 L200,1164 L110,1152 L40,1164 L0,1158 Z"/>
    </g>
  </svg>

  <svg class="cover-type" viewBox="0 0 800 1200" xmlns="http://www.w3.org/2000/svg">
    <text class="subtitle" x="400" y="124" text-anchor="middle" textLength="560" lengthAdjust="spacingAndGlyphs">THE SINGLE PATH TO HALT THE 2022</text>
    <text class="subtitle" x="404" y="158" text-anchor="middle" textLength="680" lengthAdjust="spacingAndGlyphs">PARTISAN TAKEOVER &amp; RENEW OUR HOMELAND</text>

    <text class="title-line" x="62" y="345" font-size="160" textLength="420" lengthAdjust="spacingAndGlyphs">FINAL</text>
    <text class="title-line" x="60" y="478" font-size="150" textLength="680" lengthAdjust="spacingAndGlyphs">HOUR</text>
    <text class="title-line" x="62" y="712" font-size="150" textLength="160" lengthAdjust="spacingAndGlyphs">TO</text>
    <text class="title-line" x="250" y="712" font-size="150" textLength="490" lengthAdjust="spacingAndGlyphs">RESCUE</text>
    <text class="title-line title-line--faded" x="62" y="915" font-size="130" textLength="678" lengthAdjust="spacingAndGlyphs">FREE</text>
    <text class="title-line title-line--faded" x="60" y="1028" font-size="110" textLength="680" lengthAdjust="spacingAndGlyphs">REPUBLIC</text>

    <text class="author-name" x="117" y="1136" textLength="567" lengthAdjust="spacingAndGlyphs">ROWAN ELLIS TARROW</text>
  </svg>

</main>
</body>
</html>
```